Field Mentors UK award course Flyer Design

Flyer design required for a social enterprise called "Bright Arena" - logo attached - to promote our Field Mentors Award course(s).

The course is targeted at individuals aged 13+ and will develop leadership skills that transfer beyond the sporting environment. It is a fun and practical course that focusses on leading rather than sporting ability or technical knowledge and leads on to further qualifications or awards. Individuals' self-confidence will improve and the course is a potential stepping stone in to employment, further education or training.

The course will be run at Quarrybank Community Sports Centre, Ashcombe School, Tollard Lane, Ashbury. ZX4 7QP. On Monday 20th July to Friday 24th July.
There is a subsidised fee of £15

We are a Regional Academy for Field Mentors UK.

The company's main colour is royal blue but please make the design as attractive and eye-catching to young people, male and female, as possible.

```html
<!DOCTYPE html>
<html lang="en">
<head>
<meta charset="utf-8">
<title>Field Mentors Award Course Flyer</title>
<link rel="stylesheet" href="https://fonts.googleapis.com/css2?family=Arimo:wght@400;700&display=swap">
<style>
  :root {
    --page-bg: #e6e8e4;
    --royal: #1a4fa3;
    --royal-deep: #123f8c;
    --navy-panel: #171d2c;
    --ink-navy: #1b2f6e;
    --ink-dark: #222428;
    --sky: #3aa3e0;
    --logo-disc: #8ecdf0;
    --band-text: #dfe7f4;
    --white: #ffffff;
    --rule-grey: #c9ccd2;
  }
  html, body {
    margin: 0;
    width: 1200px;
    height: 900px;
    overflow: hidden;
    background: var(--page-bg);
    font-family: "Arimo", Arial, sans-serif;
  }
  .flyer {
    position: absolute;
    left: 72px;
    top: 76px;
    width: 1056px;
    height: 747px;
    box-shadow: 0 6px 20px rgba(0,0,0,0.18);
  }
  .flyer svg { display: block; width: 100%; height: 100%; }
  .headline-lesson { fill: var(--ink-navy); font-size: 30px; }
  .headline-improvise { fill: var(--ink-dark); font-size: 30px; }
  .band-title { fill: var(--band-text); font-size: 30px; font-weight: 700; }
  .venue-name { fill: var(--white); font-size: 20px; font-weight: 700; }
  .venue-address { fill: var(--white); font-size: 17px; }
  .dates { font-size: 24px; }
  .dates .day { fill: var(--sky); font-weight: 400; }
  .dates .date { fill: var(--white); font-weight: 400; }
  .dates .joiner { fill: var(--white); font-size: 17px; }
  .cta-label { fill: var(--white); font-size: 17px; }
  .cta-url { fill: var(--white); font-size: 22px; }
  .brand-name { fill: var(--ink-navy); font-size: 19px; font-weight: 700; }
</style>
</head>
<body>
  <main class="flyer">
    <svg viewBox="0 0 886 627" xmlns="http://www.w3.org/2000/svg">
      <defs>
        <linearGradient id="photo-tones" x1="0" y1="0" x2="1" y2="1">
          <stop offset="0" stop-color="#efe6d8"/>
          <stop offset="0.35" stop-color="#c9a88e"/>
          <stop offset="0.6" stop-color="#2b3656"/>
          <stop offset="1" stop-color="#e9e2d6"/>
        </linearGradient>
      </defs>

      <rect class="photo" x="0" y="0" width="886" height="627" fill="url(#photo-tones)"
            role="img" aria-label="Photo of a girls' basketball team playing in an indoor sports hall with a scoreboard behind"/>

      <text class="headline-lesson" x="663" y="83">LESSON1:</text>
      <text class="headline-improvise" x="663" y="120">IMPROVISE.</text>

      <polygon class="wedge-left" points="0,145 300,400 300,627 0,627" fill="var(--royal)"/>
      <polygon class="wedge-left-deep" points="0,420 290,520 290,627 0,627" fill="var(--royal-deep)"/>

      <polygon class="info-panel" points="262,450 886,228 886,627 282,627" fill="var(--navy-panel)"/>

      <polygon class="title-band" points="262,372 886,150 886,228 290,446" fill="var(--royal)"/>
      <text class="band-title" transform="translate(303 413) rotate(-19.6)">FIELD MENTORS AWARD COURSE</text>

      <g transform="translate(355 478) rotate(-19.6)">
        <text class="venue-name" x="0" y="0">QUARRYBANK COMMUNITY SPORTS CENTRE</text>
        <text class="venue-address" x="52" y="28">TOLLARD LANE, ASHBURY. ZX4 7QP</text>
        <text class="dates" x="18" y="78"><tspan class="day">MONDAY</tspan><tspan class="date">20TH JULY</tspan><tspan class="joiner"> TO </tspan><tspan class="day">FRIDAY</tspan><tspan class="date">24TH JULY</tspan></text>
      </g>

      <text class="cta-label" transform="translate(616 525) rotate(-19.6)">Find out more at</text>
      <polygon class="url-band" points="545,575 886,455 886,505 560,619" fill="var(--royal)"/>
      <text class="cta-url" transform="translate(575 590) rotate(-19.6)">www.brightarena.org</text>

      <polygon class="logo-card" points="0,398 258,338 318,508 0,588" fill="var(--white)"/>
      <polygon class="logo-card-tab" points="48,578 276,528 282,560 54,612" fill="var(--white)"/>
      <line x1="38" y1="350" x2="148" y2="328" stroke="var(--white)" stroke-width="5"/>
      <line x1="38" y1="368" x2="168" y2="341" stroke="var(--white)" stroke-width="5"/>
      <line x1="0" y1="392" x2="60" y2="380" stroke="var(--rule-grey)" stroke-width="4"/>

      <circle class="brand-disc" cx="132" cy="462" r="72" fill="var(--logo-disc)"/>
      <text class="brand-name" x="132" y="469" text-anchor="middle">BRIGHT ARENA</text>
    </svg>
  </main>
</body>
</html>
```